Counseling Design Website

My husband and I are both counselors and have a business called K & J counseling. We have already purchased a logo from you in October of 2022. We both have expertise in Autism, Dyslexia, ADHD, Couples Counseling, Marriage and Family counseling, and Geriatrics. I would also like to have my forms online. I am planning on using Google sites. I have started a site, but havent gotten very far. I would like to have it created where i can just copy and paste so to speak.
https://pages.brindlehost.net/d/7kQzLp2Xv8T-NR_cY4wHaEm31PBUFsRdk/p/3HXyPq5WmA9bsjtd2EsLZFhRwGGKvTnYA/edit

```html
<!DOCTYPE html>
<html lang="en">
<head>
<meta charset="utf-8">
<title>K &amp; J Counseling</title>
<link href="https://fonts.googleapis.com/css2?family=Lato:ital,wght@0,300;0,400;0,700;1,400&display=swap" rel="stylesheet">
<style>
:root{
  --purple:#8c6cf4;
  --navy:#2d1e66;
  --ink:#2f2f3a;
  --muted:#7a7a85;
  --line:#e7e7ec;
  --soft:#f4f4f7;
  --white:#fff;
}
*{box-sizing:border-box;margin:0;padding:0}
html,body{width:1200px;height:4815px;overflow:hidden}
body{font-family:'Lato',sans-serif;color:var(--ink);background:var(--white);position:relative}
section,header,footer,nav,.topbar{position:relative;width:1200px}
.abs{position:absolute}
.btn{position:absolute;display:flex;align-items:center;justify-content:center;font-size:10px;font-weight:700;letter-spacing:.5px;text-transform:uppercase;border-radius:2px}
.btn-purple{background:var(--purple);color:var(--white)}
.btn-white{background:var(--white);color:var(--purple)}
.eyebrow{font-size:10px;font-weight:700;text-transform:uppercase;color:var(--ink);letter-spacing:.2px}
.title{font-size:28px;font-weight:300;color:var(--ink);white-space:nowrap}
.title b{font-weight:700}
.para{font-size:13px;line-height:24px;color:var(--muted)}
.photo{position:absolute}
.more{font-size:9px;font-weight:700;color:var(--purple);text-transform:uppercase;letter-spacing:.4px}

.topbar{height:34px;border-bottom:1px solid var(--line);font-size:10px;color:var(--muted)}
.topbar span{position:absolute;top:11px;white-space:nowrap}
.topbar svg{position:absolute;top:11px}
header{height:82px}
.brand{position:absolute;left:93px;top:24px;display:flex;align-items:center;gap:10px}
.brand-mark{width:24px;height:24px;background:var(--purple)}
.brand-name{font-size:26px;font-weight:400;color:var(--purple);white-space:nowrap}
.call{left:624px;top:28px;font-size:23px;color:var(--purple);font-weight:300;white-space:nowrap}
.call b{font-weight:400}
nav{height:37px;border-top:1px solid var(--line);border-bottom:1px solid var(--line)}
nav span{position:absolute;top:11px;font-size:11.5px;color:var(--ink);white-space:nowrap}
nav .active{color:var(--purple)}
.hero{height:516px;background:linear-gradient(100deg,#7f7a86 0%,#a7a2a8 45%,#cfcfd6 75%,#b9b9c3 100%)}
.hero h1{position:absolute;left:131px;top:183px;font-size:50px;line-height:62px;font-weight:400;color:var(--white)}
.hero h1 b{font-weight:700}
.services{height:352px;display:flex}
.svc{width:400px;height:352px;position:relative;padding:44px 0 0 49px}
.svc h2{font-size:32px;font-weight:400;margin-bottom:14px}
.svc p{font-size:11px;line-height:19px;width:285px;margin-bottom:10px}
.svc li{list-style:none;font-size:10px;line-height:28px;text-transform:uppercase}
.svc-adults{background:var(--navy);color:var(--white)}
.svc-children{background:var(--purple);color:var(--white)}
.svc-seniors{background:var(--soft);color:var(--ink)}
.svc-seniors p,.svc-seniors li{color:var(--muted)}
.about{height:467px}
.therapies{height:549px;background:var(--soft)}
.card-title{font-size:18px;color:var(--ink);text-align:center}
.card-text{font-size:11px;line-height:19px;color:var(--muted);text-align:center}
.stats{height:234px;background:linear-gradient(90deg,#34384a 0%,#4b5063 35%,#3c4152 65%,#595e70 100%)}
.stat{position:absolute;width:200px;text-align:center;color:var(--white)}
.stat svg{display:block;margin:0 auto 6px}
.stat .num{font-size:36px;font-weight:700;line-height:40px}
.stat .lbl{font-size:11px;margin-top:4px}
.team{height:551px}
.testimonials{height:538px;background:linear-gradient(110deg,#6f6a6c 0%,#8f8a89 40%,#a19b97 60%,#7b7577 100%)}
.testimonials .eyebrow,.testimonials .title{color:var(--white)}
.quote{position:absolute;left:240px;width:720px;font-size:16px;line-height:29px;font-style:italic;color:var(--white);text-align:center}
.news{height:695px}
.news-card{position:absolute;top:193px;width:289px;height:422px;background:var(--white);box-shadow:0 6px 22px rgba(40,40,70,.08)}
.news-card .img{height:214px}
.news-card h3{position:absolute;left:23px;top:230px;font-size:17px;font-weight:400;line-height:22px;color:var(--ink);width:240px}
.news-card .meta{position:absolute;left:23px;top:282px;font-size:9.5px;color:var(--muted);white-space:nowrap}
.news-card .ex{position:absolute;left:23px;top:308px;font-size:10.5px;line-height:19px;color:var(--muted);width:245px}
.news-card .more{position:absolute;left:23px;top:366px}
footer{height:311px;background:var(--soft)}
.fcol h4{font-size:9.5px;font-weight:700;text-transform:uppercase;margin-bottom:22px;color:var(--ink)}
.fcol p{font-size:10px;line-height:19px;color:var(--muted)}
.fcol a{display:block;font-size:10px;line-height:23px;color:var(--purple);text-decoration:none}
.copyright{position:absolute;left:0;top:273px;width:1200px;height:38px;border-top:1px solid var(--line);font-size:10px;color:var(--muted);padding:12px 0 0 142px}
</style>
</head>
<body>

<div class="topbar">
  <span style="left:146px">Visit Us Daily from 8.00 AM to 6.00 PM</span>
  <svg width="9" height="11" viewBox="0 0 10 12" style="left:551px"><path d="M5 0a4 4 0 0 0-4 4c0 3 4 8 4 8s4-5 4-8a4 4 0 0 0-4-4z" fill="var(--purple)"/><circle cx="5" cy="4" r="1.5" fill="#fff"/></svg>
  <span style="left:566px">212 Harbor Lane, Albany, NY</span>
  <svg width="11" height="9" viewBox="0 0 12 9" style="left:746px"><rect x=".5" y=".5" width="11" height="8" fill="none" stroke="var(--purple)"/><path d="M.5 .5l5.5 4 5.5-4" fill="none" stroke="var(--purple)"/></svg>
  <span style="left:765px">hello@kjcounsel.example</span>
  <span style="left:912px;color:var(--ink);font-weight:700">Request a Free Consultation</span>
</div>

<header>
  <div class="brand"><div class="brand-mark"></div><div class="brand-name">K &amp; J Counseling</div></div>
  <div class="abs call">Call: <b>800 555 0142</b></div>
  <div class="btn btn-purple" style="left:864px;top:18px;width:190px;height:43px">Make an appointment</div>
</header>

<nav>
  <span class="active" style="left:146px">Home ▾</span>
  <span style="left:215px">About ▾</span>
  <span style="left:286px">Services</span>
  <span style="left:357px">Pages ▾</span>
  <span style="left:426px">News ▾</span>
  <span style="left:493px">Forms</span>
  <span style="left:548px">Contacts</span>
  <svg class="abs" style="left:964px;top:12px" width="14" height="14" viewBox="0 0 14 14"><circle cx="6" cy="6" r="4.5" fill="none" stroke="var(--ink)" stroke-width="1.5"/><path d="M9.5 9.5l3.5 3.5" stroke="var(--ink)" stroke-width="1.5"/></svg>
  <svg class="abs" style="left:1032px;top:11px" width="13" height="15" viewBox="0 0 13 15"><rect x="1.5" y="2" width="10" height="12" fill="none" stroke="var(--ink)" stroke-width="1.4"/><path d="M4 6h5M4 9h5" stroke="var(--ink)" stroke-width="1.2"/></svg>
</nav>

<section class="hero" role="img" aria-label="Photo of a couple in a counseling session on a sofa">
  <h1>A Strong Image of<br><b>Yourself is Our Sucess</b></h1>
  <div class="btn btn-purple" style="left:142px;top:324px;width:120px;height:44px">About us</div>
  <div class="btn btn-white" style="left:279px;top:324px;width:125px;height:44px">Book now</div>
</section>

<section class="services">
  <div class="svc svc-adults">
    <h2>For Adults</h2>
    <p>You can call our highly experienced counselors if you, your partner or your family is going through difficulties.</p>
    <ul><li>Couples counseling</li><li>Marriage counseling</li><li>Family counseling</li><li>Adult ADHD</li><li>A – Z of issues</li></ul>
  </div>
  <div class="svc svc-children">
    <h2>For Children</h2>
    <p>You can call our highly experienced counselors if your child or teenager is facing learning or social challenges.</p>
    <ul><li>Autism</li><li>Dyslexia</li><li>ADHD</li><li>Family support</li><li>A-Z of issues</li></ul>
  </div>
  <div class="svc svc-seniors">
    <h2>For Seniors</h2>
    <p>You can call our highly experienced counselors for caring support through the changes that come with later life.</p>
    <ul><li>Geriatric counseling</li><li>Memory and aging</li><li>Grief and loss</li><li>Caregiver support</li><li>Family transitions</li></ul>
  </div>
</section>

<section class="about">
  <div class="photo" role="img" aria-label="Video still of a counselor shaking hands with a client" style="left:142px;top:76px;width:445px;height:320px;background:linear-gradient(120deg,#c9c4c0,#ebe7e3 55%,#b9b4b3);box-shadow:0 12px 30px rgba(0,0,0,.15)"></div>
  <svg class="abs" style="left:337px;top:208px" width="56" height="56" viewBox="0 0 56 56"><circle cx="28" cy="28" r="28" fill="#2b2b33"/><path d="M23 19l14 9-14 9z" fill="#fff"/></svg>
  <div class="abs eyebrow" style="left:635px;top:110px">Who we are</div>
  <div class="abs title" style="left:635px;top:136px">We Are The Best <b>Support for You</b></div>
  <p class="abs para" style="left:635px;top:206px;width:430px">K &amp; J Counseling is a husband and wife practice. Together we bring expertise in Autism, Dyslexia, ADHD, couples, marriage and family counseling, and geriatrics, with care for every stage of life.</p>
  <div class="btn btn-purple" style="left:635px;top:332px;width:118px;height:41px">About us</div>
</section>

<section class="therapies">
  <div class="abs eyebrow" style="left:0;width:1200px;text-align:center;top:64px">What we offer for you</div>
  <div class="abs title" style="left:0;width:1200px;text-align:center;top:92px">Therapies <b>&amp; Treatments</b></div>
  <div class="abs" style="left:575px;top:140px;width:50px;height:1px;background:var(--line)"></div>

  <div class="photo" role="img" aria-label="Photo of a smiling couple on a sofa" style="left:142px;top:183px;width:288px;height:190px;background:linear-gradient(135deg,#9fb4c9,#e4dfd8 60%,#c8b8a5)"></div>
  <div class="abs card-title" style="left:142px;width:288px;top:394px">Couples &amp; Marriage</div>
  <div class="abs card-text" style="left:152px;width:268px;top:420px">Couples therapy helps partners talk openly and rebuild trust with a counselor</div>
  <div class="abs more" style="left:142px;width:288px;text-align:center;top:475px">Learn more ›</div>

  <div class="photo" role="img" aria-label="Photo of a child working with a counselor" style="left:454px;top:183px;width:288px;height:190px;background:linear-gradient(135deg,#b5b2ad,#e9e7e3 55%,#a9a39e)"></div>
  <div class="abs card-title" style="left:454px;width:288px;top:394px">Autism, ADHD &amp; Dyslexia</div>
  <div class="abs card-text" style="left:464px;width:268px;top:420px">Support for children and families with learning and attention differences</div>
  <div class="abs more" style="left:454px;width:288px;text-align:center;top:475px">Learn more ›</div>

  <div class="photo" role="img" aria-label="Photo of an older adult talking with a counselor" style="left:766px;top:183px;width:290px;height:190px;background:linear-gradient(135deg,#7f858e,#c9cbcf 55%,#6f7680)"></div>
  <div class="abs card-title" style="left:766px;width:290px;top:394px">Geriatric Counseling</div>
  <div class="abs card-text" style="left:776px;width:270px;top:420px">Gentle care for older adults and the families who love and support them</div>
  <div class="abs more" style="left:766px;width:290px;text-align:center;top:475px">Learn more ›</div>
</section>

<section class="stats" role="img" aria-label="Dark background photo of a person in thought">
  <div class="stat" style="left:149px;top:64px">
    <svg width="44" height="40" viewBox="0 0 44 40" fill="none" stroke="#fff" stroke-width="1.5"><rect x="2" y="6" width="40" height="32"/><path d="M2 14h40M12 2v8M32 2v8"/><circle cx="22" cy="26" r="5"/></svg>
    <div class="num">30+</div><div class="lbl">Years of Experience</div>
  </div>
  <div class="stat" style="left:384px;top:64px">
    <svg width="44" height="40" viewBox="0 0 44 40" fill="none" stroke="#fff" stroke-width="1.5"><rect x="10" y="5" width="24" height="33"/><rect x="17" y="2" width="10" height="6"/><path d="M14 24h5l3-6 3 10 2-4h4"/></svg>
    <div class="num">6</div><div class="lbl">Areas of Expertise</div>
  </div>
  <div class="stat" style="left:618px;top:64px">
    <svg width="44" height="40" viewBox="0 0 44 40" fill="none" stroke="#fff" stroke-width="1.5"><circle cx="14" cy="12" r="6"/><circle cx="30" cy="12" r="6"/><path d="M3 34c0-7 5-12 11-12s11 5 11 12M19 34c0-7 5-12 11-12s11 5 11 12"/></svg>
    <div class="num">2</div><div class="lbl">Licensed Counselors</div>
  </div>
  <div class="stat" style="left:853px;top:64px">
    <svg width="44" height="40" viewBox="0 0 44 40" fill="none" stroke="#fff" stroke-width="1.5"><path d="M14 14c-3-5-10-3-10 2 0 4 10 10 10 10s10-6 10-10c0-5-7-7-10-2z"/><circle cx="30" cy="18" r="6"/><path d="M19 38c0-6 5-10 11-10s11 4 11 10"/></svg>
    <div class="num">1510</div><div class="lbl">Families Supported</div>
  </div>
</section>

<section style="height:449px">
  <div class="abs eyebrow" style="left:142px;top:90px">Online forms</div>
  <div class="abs title" style="left:142px;top:118px">Complete Your <b>Forms Online</b></div>
  <p class="abs para" style="left:142px;top:192px;width:430px">Save time before your first visit. Our intake, consent and history forms are all online, so you can fill them out from home at your own pace and send them to us securely before your session.</p>
  <div class="btn btn-purple" style="left:142px;top:313px;width:118px;height:42px">Open forms</div>
  <div class="photo" role="img" aria-label="Laptop and phone showing the online intake forms" style="left:617px;top:72px;width:440px;height:240px;background:linear-gradient(135deg,#f1f1f4,#ffffff 50%,#e8e8ee);border-radius:6px;box-shadow:0 14px 30px rgba(40,40,70,.1)"></div>
</section>

<section class="team">
  <div class="abs eyebrow" style="left:142px;top:87px">We have best team</div>
  <div class="abs title" style="left:142px;top:114px">Meet Our <b>Spesialists</b></div>
  <p class="abs para" style="left:454px;top:80px;width:602px">We think it's really important that counselors have a mixture of clinical skill and human qualities that mean you can place your trust in them. As a husband and wife team, we bring that same care to every family we work with.</p>
  <div class="photo" role="img" aria-label="Portrait of a female counselor in a grey jacket" style="left:142px;top:184px;width:289px;height:289px;background:linear-gradient(135deg,#d9d8d7,#f0efee 55%,#bdb9b6)"></div>
  <div class="photo" role="img" aria-label="Portrait of a female counselor with glasses" style="left:454px;top:184px;width:289px;height:289px;background:linear-gradient(135deg,#b7a99a,#e7ddd2 55%,#a8998c)"></div>
  <div class="photo" role="img" aria-label="Portrait of a male counselor with glasses" style="left:767px;top:184px;width:289px;height:289px;background:linear-gradient(135deg,#d8dde2,#eef0f2 55%,#8da3bd)"></div>
</section>

<section class="testimonials" role="img" aria-label="Background photo of hands held together in comfort">
  <div class="abs eyebrow" style="left:0;width:1200px;text-align:center;top:84px">Testimonials</div>
  <div class="abs title" style="left:0;width:1200px;text-align:center;top:112px">What Our <b>Clients Say</b></div>
  <p class="quote" style="top:194px">"I found the staff professional and kind, explaining the process to me every step of the way. I understand myself more clearly now and have begun to make positive changes in my life. There was such a high level of customer service."</p>
  <div class="abs" role="img" aria-label="Client avatar" style="left:566px;top:308px;width:68px;height:68px;border-radius:50%;background:linear-gradient(135deg,#cfd6de,#8b96a3);border:2px solid #fff"></div>
  <div class="abs" style="left:0;width:1200px;text-align:center;top:386px;font-size:11px;font-weight:700;color:#fff">Daniel Marsh</div>
  <div class="abs" style="left:0;width:1200px;text-align:center;top:404px;font-size:9px;color:#fff">Founder Northway Labs</div>
  <div class="abs" style="left:572px;top:474px;display:flex;gap:18px">
    <span style="width:6px;height:6px;border-radius:50%;background:rgba(255,255,255,.6)"></span>
    <span style="width:6px;height:6px;border-radius:50%;background:#fff"></span>
    <span style="width:6px;height:6px;border-radius:50%;background:#fff"></span>
  </div>
</section>

<section class="news">
  <div class="abs eyebrow" style="left:0;width:1200px;text-align:center;top:80px">Insights and news</div>
  <div class="abs title" style="left:0;width:1200px;text-align:center;top:108px">Our Latest <b>News</b></div>

  <article class="news-card" style="left:142px">
    <div class="img" role="img" aria-label="Photo of a child reading a book at a table" style="background:linear-gradient(135deg,#b8aea6,#e8e2dc 55%,#a99c93)"></div>
    <h3>Early Signs of Dyslexia in Children</h3>
    <div class="meta">February 19, 2021 &nbsp;•&nbsp; Dyslexia</div>
    <p class="ex">Reading struggles are common, so it's not always easy to know when it is...</p>
    <div class="more">Learn more ›</div>
  </article>
  <article class="news-card" style="left:454px">
    <div class="img" role="img" aria-label="Photo of a couple talking on a sofa" style="background:linear-gradient(135deg,#a5a19d,#dcd8d3 55%,#8f8a86)"></div>
    <h3>Is It Time for Couples Counseling?</h3>
    <div class="meta">February 1, 2021 &nbsp;•&nbsp; Marriage, Family</div>
    <p class="ex">Every couple argues from time to time, so it's not always easy to know when it is...</p>
    <div class="more">Learn more ›</div>
  </article>
  <article class="news-card" style="left:767px">
    <div class="img" role="img" aria-label="Photo of an older adult holding hands with a family member" style="background:linear-gradient(135deg,#8e8e92,#d6d6d8 55%,#6f6f74)"></div>
    <h3>Supporting Aging Parents at Home</h3>
    <div class="meta">February 1, 2021 &nbsp;•&nbsp; Geriatrics</div>
    <p class="ex">Caring for a parent brings change, so it's not always easy to know when it is...</p>
    <div class="more">Learn more ›</div>
  </article>
</section>

<footer>
  <div class="abs" style="left:142px;top:30px;display:flex;align-items:center;gap:8px"><div class="brand-mark" style="width:20px;height:20px"></div><div style="font-size:21px;color:var(--purple);white-space:nowrap">K &amp; J Counseling</div></div>
  <p class="abs" style="left:142px;top:86px;width:200px;font-size:10px;line-height:19px;color:var(--muted)">A husband and wife counseling practice caring for children, couples, families and seniors.</p>
  <div class="abs" style="left:142px;top:190px;display:flex;gap:16px">
    <span style="width:9px;height:9px;border-radius:50%;background:#b9b9c3"></span>
    <span style="width:9px;height:9px;border-radius:50%;background:#b9b9c3"></span>
    <span style="width:9px;height:9px;border-radius:50%;background:#b9b9c3"></span>
    <span style="width:9px;height:9px;border-radius:50%;background:#b9b9c3"></span>
  </div>

  <div class="abs fcol" style="left:378px;top:56px">
    <h4>Our head clinick</h4>
    <p>212 Harbor Lane, Albany, NY 12207<br>United States of America<br>hello@kjcounsel.example<br>518 555 0179<br>We Work for You Every Day<br>from <b style="color:var(--ink)">8.00 AM</b> to <b style="color:var(--ink)">6.00 PM</b></p>
  </div>
  <div class="abs fcol" style="left:611px;top:56px;width:200px">
    <h4>Latest news</h4>
    <p style="color:var(--ink)">Early Signs of Dyslexia in Children</p>
    <p style="font-size:9px;margin-bottom:14px">February 19, 2021</p>
    <p style="color:var(--ink)">Is It Time for Couples Counseling?</p>
    <p style="font-size:9px">February 1, 2021</p>
  </div>
  <div class="abs fcol" style="left:845px;top:56px">
    <h4>Quick links</h4>
    <a>Home</a><a>About</a><a>Services</a><a>Forms</a><a>News</a><a>Contacts</a>
  </div>
  <div class="copyright">© 2023 All Rights Reserved.</div>
</footer>

</body>
</html>
```